Brindle.vc needs a better website design!

We need a new and better website for Brindle.vc. We're a Canadian venture capital firm that invests in innovative entrepreneurs. We compete against the following websites: tollery.vc, quorbinvest.ca, gavelvc.com, and duskara.vc. We're a diverse group of partners and we're dedicated to the founders we invest in.
Updates

I don’t really like stock photos of random people as part of the website design…so please try to stay away from using those images. Thanks, Owen

Target Market(s)

Canadian entrepreneurs and investors

Industry/Entity Type

Venture capital, finance, investment, entrepreneurship

Coding

Coded - Design and coding required

Number of Pages Required

4 page

Font styles to use
Sans Serif

Colors

Designer to choose colors to be used in the design.

Requirements
Must have
• Clean crisp overall design. Fast and to the point.
Nice to have
• Check out www.brindle.vc - I did it myself and it is too basic and too wordy.
Should not have
• No stock images with random people in them! Not too wordy or with too many large images that are slow to load.

```html
<!DOCTYPE html>
<html lang="en">
<head>
<meta charset="utf-8">
<title>Brindle.vc – What We Look For</title>
<link href="https://fonts.googleapis.com/css2?family=Poppins:wght@400;500;600&display=swap" rel="stylesheet">
<style>
:root{
  --green:#7b9a2d;
  --ink:#1f2116;
  --text:#2b2b2b;
  --muted:#6c6c6c;
  --line:#d9d9d9;
  --footer-bg:#f4f4f4;
  --bar-bg:#232323;
  --nav-active:#f1f1f1;
  --icon:#9a9a9a;
}
*{margin:0;padding:0;box-sizing:border-box}
html,body{width:894px;height:1200px;overflow:hidden}
body{font-family:'Poppins',sans-serif;background:#fff;color:var(--text);position:relative}
.abs{position:absolute}

.site-header{position:absolute;left:0;top:0;width:894px;height:73px;background:#fff}
.brand{position:absolute;left:120px;top:22px;display:flex;align-items:center;gap:6px;font-size:14px;font-weight:600;color:var(--green);letter-spacing:.5px}
.brand-dot{width:16px;height:16px;border-radius:50%;border:2px solid var(--green)}
.main-nav a{position:absolute;top:29px;font-size:10px;color:#444;text-decoration:none}
.main-nav .active-tab{position:absolute;left:676px;top:0;width:106px;height:76px;background:var(--nav-active);border-bottom:3px solid var(--green)}
.main-nav a.active{color:var(--green)}

.hero{position:absolute;left:0;top:73px;width:894px;height:234px;
  background:linear-gradient(180deg,#8a9088 0%,#5d6b58 35%,#3c5535 70%,#2c4426 100%)}
.hero-wave{position:absolute;left:0;top:230px}
.hero-title{position:absolute;left:0;top:124px;width:894px;text-align:center;color:#fff;font-size:17.5px;font-weight:600;line-height:28.5px}

.breadcrumb{position:absolute;left:121px;top:277px;font-size:10px;color:#555}
.breadcrumb .sep{margin:0 6px;color:#777}
.breadcrumb .current{color:var(--green)}

.page-title{position:absolute;left:0;top:338px;width:894px;text-align:center;font-size:20px;font-weight:600;color:var(--ink)}
.section-lead{position:absolute;left:121px;font-size:14.5px;color:var(--ink)}
.criteria{position:absolute;left:120px;display:flex;align-items:center}
.criteria svg{width:28px;height:28px;flex:none;margin-right:9px}
.criteria p{font-size:10px;color:var(--muted)}
.criteria b{font-weight:400;color:var(--text)}
.divider{position:absolute;left:120px;top:552px;width:654px;border-top:1px dashed var(--line)}

.site-footer{position:absolute;left:0;top:965px;width:894px;height:202px;background:var(--footer-bg)}
.footer-brand{position:absolute;left:120px;top:1050px;display:flex;align-items:center;gap:10px;font-size:24px;font-weight:600;color:var(--green)}
.footer-brand .brand-dot{width:30px;height:30px;border-width:3px}
.footer-heading{position:absolute;font-size:15.5px;font-weight:500;color:var(--ink)}
.quick-links a{position:absolute;left:388px;font-size:10px;color:#333;text-decoration:none}
.quick-links a::before{content:"›";margin-right:8px;color:#555}
.quick-links a.active{color:var(--green)}
.quick-links a.active::before{color:var(--green)}
.contact-mail{position:absolute;left:634px;top:1037px;display:flex;align-items:center;gap:7px;font-size:10px;color:#333}
.social{position:absolute;top:1099px;width:22px;height:22px;border-radius:50%}
.copyright{position:absolute;left:0;top:1167px;width:894px;height:33px;background:var(--bar-bg);color:#fff;font-size:10px;text-align:center;line-height:33px;font-weight:500}
</style>
</head>
<body>

<header class="site-header">
  <div class="brand"><span class="brand-dot"></span>BRINDLE.VC</div>
  <nav class="main-nav">
    <div class="active-tab"></div>
    <a href="#" style="left:444px">Home</a>
    <a href="#" style="left:515px">Team</a>
    <a href="#" style="left:584px">Companies</a>
    <a href="#" class="active" style="left:685px">What We Look For</a>
  </nav>
</header>

<section class="hero" role="img" aria-label="Misty green forested mountains under a grey sky">
</section>
<svg class="hero-wave" width="894" height="80" viewBox="0 230 894 80" aria-hidden="true">
  <path d="M0 281 C80 250 160 240 240 246 C380 256 470 312 620 307 C740 303 820 285 894 278 L894 310 L0 310 Z" fill="#fff"/>
</svg>
<h1 class="hero-title">Brindle.vc is a venture capital firm that invests in innovative<br>seed-stage technology companies in Western Canada<br>focused on B2B and SaaS markets.</h1>

<div class="breadcrumb">Home<span class="sep">»</span><span class="current">What We Look For</span></div>

<h2 class="page-title">What We Look For</h2>
<h3 class="section-lead" style="top:378px;font-weight:400">We invest in innovative technology companies with these characteristics:</h3>

<div class="criteria" style="top:413px">
  <svg viewBox="0 0 28 28" fill="none" stroke="var(--icon)" stroke-width="1"><circle cx="14" cy="5" r="3"/><path d="M9 13c0-3 10-3 10 0"/><circle cx="5" cy="19" r="3"/><circle cx="23" cy="19" r="3"/><path d="M0.5 27c0-3 9-3 9 0M18.5 27c0-3 9-3 9 0"/><circle cx="14" cy="19" r="2.5" stroke="var(--green)"/></svg>
  <p><b>Founding Team:</b> Visionary, Committed, Coachable, Skilled, Aligned, With Market Fit</p>
</div>
<div class="criteria" style="top:456px">
  <svg viewBox="0 0 28 28" fill="none" stroke="var(--icon)" stroke-width="1"><circle cx="16" cy="11" r="9"/><path d="M9 18l-7 7"/><path d="M12 15v-5M15 15v-7M18 15v-4M21 15v-6"/><circle cx="22" cy="22" r="3.5" stroke="var(--green)"/></svg>
  <p><b>Total Addressable Market:</b> Large, Growing, and Attractive; With a Manageable Competitive Landscape</p>
</div>
<div class="criteria" style="top:500px">
  <svg viewBox="0 0 28 28" fill="none" stroke="var(--icon)" stroke-width="1"><path d="M2 27h25M4 27v-4M8 27v-7M12 27v-9M16 27v-12M20 27v-14M24 27v-16"/><circle cx="21" cy="6" r="4.5" stroke="var(--green)"/><path d="M3 10v5M7 8v5M11 6v5" stroke="var(--green)"/></svg>
  <p><b>Product Market Fit:</b> MVP + Initial Market Validation; Early Revenue and Growth Potential</p>
</div>

<div class="divider"></div>

<h3 class="section-lead" style="top:570px;font-weight:400">Other things we consider in evaluating our venture capital investments:</h3>

<div class="criteria" style="top:601px">
  <svg viewBox="0 0 28 28" fill="none" stroke="var(--icon)" stroke-width="1"><circle cx="14" cy="14" r="13"/><path d="M9 13l5 4 6-9" stroke="var(--green)"/></svg>
  <p><b>Timing:</b> Supportive Market Trends; Not Too Early or Too Late, Just Right</p>
</div>
<div class="criteria" style="top:646px">
  <svg viewBox="0 0 28 28" fill="none" stroke="var(--icon)" stroke-width="1"><path d="M14 2L27 26H1Z"/><path d="M14 10v8" stroke="var(--green)"/><circle cx="14" cy="22" r="1" stroke="var(--green)"/></svg>
  <p><b>Problem:</b> Big Pain; Customers Care About It + Are Willing to Pay</p>
</div>
<div class="criteria" style="top:690px">
  <svg viewBox="0 0 28 28" fill="none" stroke="var(--icon)" stroke-width="1"><circle cx="14" cy="9" r="5"/><path d="M4 27c0-8 20-8 20 0"/><circle cx="5" cy="7" r="3"/><circle cx="23" cy="7" r="3"/><path d="M11 27v-5h6v5" stroke="var(--green)"/></svg>
  <p><b>Customers:</b> Understand Who + How to Reach; Realistic Go to Market Strategy</p>
</div>
<div class="criteria" style="top:735px">
  <svg viewBox="0 0 28 28" fill="none" stroke="var(--icon)" stroke-width="1"><rect x="11" y="1" width="6" height="4"/><path d="M14 5v4M4 13h20M4 13v5M14 13v5M24 13v5M14 9l3 2-3 2-3-2z"/><circle cx="4" cy="23" r="3" stroke="var(--green)"/><circle cx="16" cy="23" r="3" stroke="var(--green)"/><circle cx="24" cy="23" r="3" stroke="var(--green)"/></svg>
  <p><b>Business Model:</b> Clear + Compelling; Increasing Scale Returns; Realizable Projections</p>
</div>
<div class="criteria" style="top:786px">
  <svg viewBox="0 0 28 28" fill="none" stroke="var(--icon)" stroke-width="1"><path d="M2 10v8l6 6v3M26 10v8l-6 6v3"/><path d="M10 3v10M14 1v12M18 3v10" stroke="var(--green)"/></svg>
  <p><b>Competitive Advantage:</b> Secret Sauce / Protective Moat for Product or Technology</p>
</div>
<div class="criteria" style="top:836px">
  <svg viewBox="0 0 28 28" fill="none" stroke="var(--icon)" stroke-width="1"><circle cx="19" cy="7" r="6" stroke="var(--green)"/><path d="M1 19h6v8H1M7 21h8l10-4-3 6-15 2"/></svg>
  <p><b>Funding:</b> Smart Use; Enough to Reach Milestones; Series A Potential; Exit Opportunities</p>
</div>
<div class="criteria" style="top:880px">
  <svg viewBox="0 0 28 28" fill="none" stroke="var(--icon)" stroke-width="1"><path d="M2 1h15l5 5v20H2z"/><path d="M5 7h9M5 11h12"/><path d="M8 21l5-4 4 3 5-4 4 5-5 4z" stroke="var(--green)"/></svg>
  <p><b>Deal Terms:</b> Valuation, Investment Amount, % Ownership; Cap Table; USA Terms</p>
</div>

<footer class="site-footer"></footer>
<div class="footer-brand"><span class="brand-dot"></span>BRINDLE.VC</div>

<h4 class="footer-heading" style="left:388px;top:1005px">Quick Links</h4>
<nav class="quick-links">
  <a href="#" style="top:1037px">Home</a>
  <a href="#" style="top:1061px">Team</a>
  <a href="#" style="top:1085px">Companies</a>
  <a href="#" class="active" style="top:1109px">What We Look For</a>
</nav>

<h4 class="footer-heading" style="left:635px;top:1006px">Get In Touch</h4>
<div class="contact-mail">
  <svg width="11" height="8" viewBox="0 0 11 8"><rect width="11" height="8" fill="var(--green)"/><path d="M0 0l5.5 4.5L11 0" stroke="#fff" fill="none" stroke-width="1"/></svg>
  info@brindle.vc
</div>
<h4 class="footer-heading" style="left:635px;top:1069px">Follow Us</h4>
<span class="social" style="left:636px;background:#18c6e6" role="img" aria-label="Social profile link"></span>
<span class="social" style="left:663px;background:#1c8fc4" role="img" aria-label="Professional network profile link"></span>

<div class="copyright">Copyright © 2021 Brindle.vc - All Rights Reserved.</div>

</body>
</html>
```